Brightvale Energy International Website

Brightvale Energy – Lighting the Path of
UK Homes Sustainably.

New Launch Website

Focus on 4 Product Categories

- Solar PV
- Battery Energy Storage
- EV Charging
- Heat Pumps

Add

Energy News
Enquire Now button Top right every page
Contact us page

Follow Lumenhaus.co.uk for similar content pages

Target Market(s)

Residential home owners UK NOT US

Industry/Entity Type

Solar energy, home energy , EV charging

Coding

Coded - Design and coding required

Number of Pages Required

5+ page

Font styles to use
Sans Serif

Colors
0054AA
0677BA
7BADD7
CADEEF
E8F1F8
59FF00
82FF00
B8FF75
E3FFCB
F4FFEA
FFF300
FFF600
FEFA6F
FFFEC7
FFFEE8

Requirements
Must have
• Strong brand logo on every page, clear content bar
Nice to have
• Add these logos from LumenHaus.co.uk

```html
<!DOCTYPE html>
<html lang="en">
<head>
<meta charset="utf-8">
<title>Brightvale Energy – Home</title>
<link href="https://fonts.googleapis.com/css2?family=Poppins:wght@400;500;600;700&display=swap" rel="stylesheet">
<style>
:root{
  --green:#62bd45;
  --green-soft:#e6f5df;
  --orange:#f2a51c;
  --teal:#0f4a50;
  --teal-deep:#0a3a40;
  --ink:#173c44;
  --muted:#7c8a8d;
  --line:#e4ecec;
  --grey:#f4f6f6;
  --white:#ffffff;
}
*{box-sizing:border-box;margin:0;padding:0}
html,body{width:1200px;height:1200px;overflow:hidden;background:var(--white)}
body{font-family:"Poppins",sans-serif;color:var(--ink);position:relative}
.page{position:absolute;left:520px;top:0;width:512px;height:3864px;transform:scale(.3106);transform-origin:0 0;overflow:hidden;background:var(--white)}
.wrap{padding:0 36px;position:relative;height:100%}
.tag{display:inline-flex;align-items:center;gap:4px;background:var(--green);color:#fff;font-size:6px;font-weight:600;padding:2px 6px;border-radius:3px}
.tag::before{content:"";width:6px;height:6px;border-radius:2px;background:#fff}
.h2{font-size:17px;font-weight:700;line-height:1.2;color:var(--ink)}
.h2 em{font-style:normal;color:var(--green)}
.on-dark .h2,.on-dark{color:#fff}
.center{text-align:center}
.p{font-size:5.5px;line-height:1.6;color:var(--muted)}
.on-dark .p{color:#c7dadb}
.btn{display:inline-block;background:var(--green);color:#fff;font-size:6px;font-weight:600;padding:5px 10px;border-radius:3px}
.btn::after{content:" ↗"}
.btn.orange{background:var(--orange)}
.underline{width:30px;height:2px;background:var(--green);margin:6px auto 0}
.icon{width:20px;height:20px;border-radius:50%;background:var(--green);flex:none}
.icon.ring{background:#fff;border:2px solid var(--green)}

.topbar{height:16px;background:var(--green);display:flex;align-items:center;justify-content:space-between;padding:0 36px;font-size:5px;color:#fff}
.topbar .dark{background:var(--teal-deep);height:100%;display:flex;align-items:center;margin-left:-36px;padding-left:36px;gap:10px;clip-path:polygon(0 0,100% 0,94% 100%,0 100%);width:260px}
.topbar .social{display:flex;gap:4px;align-items:center}
.topbar .social i{width:6px;height:6px;border-radius:50%;background:#fff;display:block}
.nav{height:36px;display:flex;align-items:center;justify-content:space-between;padding:0 36px}
.brand{font-size:9px;font-weight:700;color:var(--teal)}
.brand span{color:var(--green)}
.menu{display:flex;gap:9px;font-size:5.5px;font-weight:600;color:var(--ink)}
.nav .btn{font-size:5.5px;padding:4px 8px}

.hero{height:270px;position:relative;background:linear-gradient(100deg,#163f3a 0%,#3d6a4d 45%,#7c8f5a 70%,#5a7d8d 100%)}
.hero-shade{position:absolute;inset:0;background:linear-gradient(90deg,rgba(8,40,44,.85) 0%,rgba(8,40,44,.45) 55%,rgba(8,40,44,0) 80%)}
.hero-copy{position:absolute;left:36px;top:38px;width:220px;color:#fff}
.hero-copy .kicker{font-size:6px;letter-spacing:2px;font-weight:700;color:var(--green);margin-bottom:8px}
.hero-copy h1{font-size:21px;line-height:1.28;font-weight:700}
.hero-copy h1 .out{color:transparent;-webkit-text-stroke:.6px #fff}
.hero-copy .p{color:#dfe9e6;margin:10px 0 12px}
.hero-copy .btn{margin-right:6px}
.arrow{position:absolute;top:116px;width:18px;height:18px;border-radius:50%;background:#fff;color:var(--teal);font-size:9px;display:flex;align-items:center;justify-content:center}
.features{position:absolute;left:36px;right:36px;top:234px;display:flex;gap:10px}
.feature{flex:1;height:72px;background:var(--teal);border-radius:8px;padding:10px;display:flex;gap:7px;color:#fff}
.feature h3{font-size:7px;font-weight:600;margin-bottom:3px}
.feature .p{color:#bcd3d3;font-size:4.6px}

.about{height:320px;padding-top:78px}
.about .wrap{display:flex;gap:22px}
.about-art{width:202px;height:196px;position:relative}
.about-art .a{position:absolute;left:0;top:0;width:100px;height:196px;border-radius:50px;background:linear-gradient(180deg,#6ea6d8,#7fb866 55%,#3d6e99)}
.about-art .b{position:absolute;left:104px;top:10px;width:98px;height:186px;border-radius:49px;background:linear-gradient(180deg,#c9d8dc,#e2e6e3 40%,#56616a)}
.about-art .ring{position:absolute;left:72px;top:0;width:130px;height:196px;border:3px solid var(--green);border-radius:65px}
.about-art .badge{position:absolute;left:72px;top:66px;width:56px;height:56px;border-radius:50%;background:var(--green);border:4px solid #fff;color:#fff;text-align:center;padding-top:12px;font-size:14px;font-weight:700;line-height:1}
.about-art .badge small{display:block;font-size:4.5px;font-weight:500}
.about-copy{flex:1}
.about-copy .h2{margin:6px 0 8px}
.pair{display:flex;gap:12px;margin:18px 0}
.pair div{display:flex;gap:6px;flex:1}
.pair h4{font-size:6px;font-weight:600}

.services{height:228px;background:var(--teal)}
.services .wrap{display:flex;gap:12px;padding-top:30px}
.services-intro{width:102px}
.services-intro .h2{margin:6px 0 8px;font-size:15px}
.services-intro .btn{margin-top:12px}
.svc{width:102px;height:160px;background:#fff;border-radius:8px;padding:4px;position:relative}
.svc .img{height:62px;border-radius:6px;background:linear-gradient(180deg,#6c9fe0,#3a5ea8 60%,#27478a)}
.svc .icon{position:absolute;left:8px;top:50px;width:18px;height:18px;border:2px solid #fff}
.svc h4{font-size:7px;font-weight:600;margin:12px 4px 2px}
.svc .p{font-size:4.5px;margin:0 4px}
.svc ul{list-style:none;font-size:4.5px;color:var(--muted);margin:6px 4px;line-height:1.7}
.svc .btn{margin:2px 4px;font-size:5px;padding:4px 7px}

.steps{height:240px;padding-top:46px}
.steps .h2{margin:8px 0 0}
.step-row{display:flex;gap:12px;margin-top:28px}
.step{flex:1;height:82px;border-radius:6px;box-shadow:0 2px 8px rgba(15,74,80,.12);padding:10px 8px;position:relative}
.step .pill{background:var(--teal);color:#fff;font-size:5.5px;font-weight:600;text-align:center;border-radius:8px;padding:3px;width:70%}
.step .icon{position:absolute;right:4px;top:-4px;width:22px;height:22px;border:2px solid #fff}
.step h4{font-size:6.5px;font-weight:600;margin:10px 0 3px}

.skills{height:288px;padding-top:22px}
.skills .wrap{display:flex;gap:22px}
.skills-art{width:202px;height:222px;position:relative}
.skills-art::before{content:"";position:absolute;left:-6px;top:0;width:210px;height:222px;border-radius:26px;background:var(--green-soft);transform:rotate(-3deg)}
.skills-art .img{position:absolute;inset:0;border-radius:24px;background:linear-gradient(180deg,#5c97d8 0%,#8fb77a 30%,#2d4f86 55%,#c36e52 100%)}
.skills-copy{flex:1}
.skills-copy .h2{margin:6px 0 8px}
.bar{margin-top:14px}
.bar .row{display:flex;justify-content:space-between;font-size:5.5px;font-weight:600}
.bar .track{height:3px;background:var(--line);margin-top:5px}
.bar .fill{height:100%;background:var(--green)}
.skills-copy .btn{margin-top:18px}

.portfolio{height:292px;position:relative}
.portfolio::before{content:"";position:absolute;left:0;right:0;top:0;height:188px;background:linear-gradient(180deg,#16525a,var(--teal))}
.portfolio .wrap{padding-top:46px}
.portfolio .h2{margin-top:6px;color:#fff}
.folio-row{display:flex;gap:10px;margin-top:20px}
.folio{flex:1}
.folio .img{height:124px;border-radius:14px 14px 6px 6px}
.folio .cap{display:flex;justify-content:space-between;align-items:center;margin-top:6px}
.folio small{display:block;font-size:4px;color:var(--green);letter-spacing:.5px}
.folio b{font-size:6px;font-weight:600}
.folio .go{width:16px;height:16px;border-radius:50%;background:var(--green);color:#fff;font-size:8px;display:flex;align-items:center;justify-content:center}

.pricing{height:354px;padding-top:30px}
.pricing .h2{margin-top:8px}
.plans{display:flex;gap:14px;margin-top:28px}
.plan{flex:1;height:200px;border-radius:8px;box-shadow:0 2px 10px rgba(15,74,80,.1);padding:14px;position:relative}
.plan.featured{border:2px solid var(--green)}
.plan .flag{position:absolute;right:0;top:6px;background:var(--green);color:#fff;font-size:6px;font-weight:600;padding:2px 8px;border-radius:2px}
.plan .price{font-size:18px;font-weight:700;margin-top:4px}
.plan .price small{font-size:5px;font-weight:500}
.plan .btn{display:block;text-align:center;margin:12px 0 18px}
.plan ul{list-style:none;font-size:5px;color:var(--ink);line-height:3.2}
.plan li::before{content:"✓";display:inline-block;width:7px;height:7px;border-radius:50%;background:var(--green);color:#fff;font-size:4px;text-align:center;line-height:7px;margin-right:4px}

.stats{height:78px;background:var(--teal)}
.stats .wrap{display:flex;align-items:center}
.stat{flex:1;display:flex;gap:6px;align-items:center;padding-left:8px;border-left:1px solid rgba(255,255,255,.25);color:#fff}
.stat:first-child{border:0}
.stat .icon{width:28px;height:28px;background:#fff;border:3px solid var(--green)}
.stat b{font-size:15px;font-weight:700}
.stat b sup{color:var(--green);font-size:7px}
.stat small{display:block;font-size:4.5px}

.team{height:250px;padding-top:38px}
.team .h2{margin-top:8px}
.members{display:flex;justify-content:space-between;margin-top:26px}
.member{width:80px;text-align:center;position:relative}
.member .img{width:80px;height:80px;border-radius:50%}
.member .plus{position:absolute;right:-2px;top:58px;width:16px;height:16px;border-radius:50%;background:var(--green);border:2px solid #fff}
.member b{display:block;font-size:6px;font-weight:600;margin-top:8px}
.member small{font-size:4.5px;color:var(--green)}

.quote{height:220px;background:var(--grey);display:flex}
.quote-img{width:246px;height:204px;position:relative;background:linear-gradient(180deg,#6ea3e2 0%,#a9c9ec 35%,#3b5fa4 60%,#27447e 100%)}
.quote-img .play{position:absolute;left:106px;top:88px;width:30px;height:30px;border-radius:50%;background:var(--green);border:3px solid #fff}
.quote-form{flex:1;padding:16px 36px 0 14px}
.quote-form h3{font-size:9px;font-weight:600}
.fields{display:grid;grid-template-columns:1fr 1fr;gap:8px;margin-top:14px}
.field{height:20px;background:#fff;border-radius:3px;font-size:5px;color:var(--muted);padding:7px 10px}
.field.wide{grid-column:1/3;height:46px}
.quote-form .btn{margin-top:10px}

.sustain{height:168px;background:linear-gradient(180deg,#1b5f64,var(--teal));position:relative}
.sustain .wrap{padding-top:26px;text-align:center}
.sustain .h2{color:#fff;font-size:15px}
.sustain .p{margin:6px auto 10px;width:260px}
.logos{position:absolute;left:36px;right:36px;bottom:-12px;height:40px;background:#fff;border-radius:8px;display:flex;align-items:center;justify-content:space-around;box-shadow:0 2px 8px rgba(0,0,0,.08)}
.logos span{font-size:11px;font-weight:600;color:var(--teal);display:flex;align-items:center;gap:3px}
.logos span::before{content:"";width:10px;height:10px;border-radius:50%;background:var(--green)}

.why{height:324px;padding-top:52px}
.why .wrap{display:flex;gap:14px}
.why-copy{width:236px}
.why-copy .h2{margin:6px 0 8px;white-space:nowrap}
.reason{display:flex;gap:8px;margin-top:16px}
.reason h4{font-size:6px;font-weight:600;margin-bottom:2px}
.why-art{flex:1;position:relative;height:222px}
.why-art .a{position:absolute;right:0;top:0;width:152px;height:168px;border-radius:10px 10px 60px 10px;background:linear-gradient(180deg,#5c99d6,#a7c9e6 50%,#5f9c3c)}
.why-art .b{position:absolute;left:0;top:112px;width:110px;height:110px;border-radius:10px 40px 10px 10px;background:linear-gradient(180deg,#7aa8d6,#3d5f98 50%,#c06a45);border:4px solid #fff}

.testi{height:210px;background:var(--teal)}
.testi .wrap{display:flex;gap:12px;padding-top:28px}
.testi-intro{width:140px}
.testi-intro .h2{font-size:15px;margin:6px 0 8px}
.testi-intro .btn{margin-top:10px}
.review{flex:1;height:118px;background:#fff;border-radius:10px;padding:12px;position:relative;color:var(--ink)}
.review .stars{color:var(--orange);font-size:6px;letter-spacing:1px}
.review q{display:block;font-size:5.5px;font-style:italic;font-weight:500;line-height:1.6;margin:6px 0;quotes:none;color:var(--ink)}
.review b{font-size:6px;font-weight:600;display:block;border-left:2px solid var(--green);padding-left:4px}
.review small{font-size:4.5px;color:var(--green);padding-left:6px}
.review .av{position:absolute;right:10px;bottom:8px;width:20px;height:20px;border-radius:50%;background:#c9d6d8;border:2px solid var(--green)}
.dots{position:absolute;left:330px;top:164px;display:flex;gap:3px}
.dots i{width:4px;height:4px;border-radius:50%;background:#9bb5b6}
.dots i:first-child{background:var(--green)}

.blog{height:360px;padding-top:42px}
.blog .h2{margin-top:8px}
.posts{display:flex;gap:12px;margin-top:22px}
.post{flex:1;height:202px;border-radius:6px;box-shadow:0 2px 10px rgba(15,74,80,.1);padding:8px}
.post .img{height:86px;border-radius:4px;position:relative}
.post .date{position:absolute;right:4px;bottom:-4px;background:var(--green);color:#fff;font-size:4.5px;padding:2px 5px;border-radius:2px}
.post .meta{font-size:4.5px;color:var(--muted);margin:10px 0 6px}
.post h4{font-size:7px;font-weight:600;line-height:1.3;margin-bottom:5px}
.post .btn{margin-top:10px;font-size:5px;padding:4px 7px}

.footer{height:210px;background:var(--teal-deep);color:#fff;position:relative}
.footer .wrap{display:flex;padding-top:36px;gap:20px}
.foot-brand{width:166px}
.foot-brand .brand{color:#fff;font-size:9px}
.foot-brand .p{margin:10px 0}
.foot-brand h5,.foot-col h5{font-size:6.5px;font-weight:600;margin-bottom:8px}
.sub{display:flex;justify-content:space-between;align-items:center;border-bottom:1px solid rgba(255,255,255,.3);padding:4px 0;font-size:5px;color:#c7dadb}
.sub .btn{font-size:5px;padding:3px 7px}
.foot-col{flex:1}
.foot-col ul{list-style:none;font-size:5px;color:#c7dadb;line-height:2.8}
.contact{display:flex;gap:5px;margin-bottom:8px;font-size:4.6px;color:#c7dadb;line-height:1.5}
.contact .icon{width:12px;height:12px}
.contact b{color:#fff;font-weight:600}
.foot-bottom{position:absolute;left:36px;right:36px;top:184px;display:flex;justify-content:space-between;font-size:4.5px;color:#c7dadb}
.foot-bottom .social{display:flex;gap:4px}
.foot-bottom .social i{width:10px;height:10px;border-radius:50%;background:#fff;display:block}
</style>
</head>
<body>
<div class="page">

  <div class="topbar">
    <div class="dark"><span>✉ hello@brightvaleenergy.co.uk</span><span>✆ +44 20 7946 0321</span><span>◷ Sun - Fri (8AM - 7PM)</span></div>
    <div class="social">Follow Us <i></i><i></i><i></i><i></i></div>
  </div>

  <header class="nav">
    <div class="brand">Brightvale <span>Energy</span></div>
    <nav class="menu"><span>Home</span><span>Solar PV</span><span>Battery Energy Storage</span><span>EV Charging</span><span>Heat Pumps</span><span>Energy News</span><span>Contact Us</span></nav>
    <span class="btn">Enquire Now</span>
  </header>

  <section class="hero" role="img" aria-label="Installer fitting solar panels on a sunny roof">
    <div class="hero-shade"></div>
    <div class="arrow" style="left:16px">←</div>
    <div class="arrow" style="right:16px">→</div>
    <div class="hero-copy">
      <div class="kicker">WELCOME TO BRIGHTVALE ENERGY</div>
      <h1>We Provide Best<br>Solar &amp; <span class="out">Renewable</span><br>Energy For You</h1>
      <p class="p">Clean, reliable power for UK homes, designed and fitted by our trusted local team.</p>
      <span class="btn">Read More</span><span class="btn orange">Learn More</span>
    </div>
    <div class="features">
      <div class="feature"><div class="icon"></div><div><h3>Experts Staff</h3><p class="p">Certified installers who plan every system to suit your home and budget.</p></div></div>
      <div class="feature"><div class="icon"></div><div><h3>Affordable Pricing</h3><p class="p">Clear, fixed quotes with flexible finance so savings start from day one.</p></div></div>
      <div class="feature"><div class="icon"></div><div><h3>24/7 Support</h3><p class="p">Friendly help whenever you need it, from first call to aftercare checks.</p></div></div>
    </div>
  </section>

  <section class="about">
    <div class="wrap">
      <div class="about-art">
        <div class="a" role="img" aria-label="Wind turbines over green fields and solar panels"></div>
        <div class="b" role="img" aria-label="Engineer holding a solar panel"></div>
        <div class="ring"></div>
        <div class="badge">30+<small>Years Of Experience</small></div>
      </div>
      <div class="about-copy">
        <span class="tag">About Us</span>
        <h2 class="h2">We Are The Best &amp; Expert<br>For <em>Your Solar</em> Solution</h2>
        <p class="p">We help homeowners cut bills and carbon with solar, storage, EV charging and heat pumps, all installed to the highest UK standards.</p>
        <div class="pair">
          <div><span class="icon ring"></span><span><h4>Easy Installation</h4><p class="p">Quick, tidy fitting with no fuss.</p></span></div>
          <div><span class="icon ring"></span><span><h4>Quality Material</h4><p class="p">Tier one panels and parts only.</p></span></div>
        </div>
        <span class="btn">Discover More</span>
      </div>
    </div>
  </section>

  <section class="services on-dark">
    <div class="wrap">
      <div class="services-intro">
        <span class="tag">Services</span>
        <h2 class="h2">Let's Check<br>Our <em>Services</em></h2>
        <p class="p">From panels to pumps, we design complete home energy systems that keep costs low and comfort high all year.</p>
        <span class="btn">All Services</span>
      </div>
      <div class="svc"><div class="img" role="img" aria-label="Solar panel array under blue sky"></div><span class="icon"></span><h4 style="color:var(--ink)">Solar &amp; Battery</h4><p class="p">Store what you make.</p><ul><li>1. Free assessment visit</li><li>2. Smart battery sizing</li><li>3. Premium 10 year cover</li></ul><span class="btn">Learn More</span></div>
      <div class="svc"><div class="img" role="img" aria-label="Solar panel array under blue sky"></div><span class="icon"></span><h4 style="color:var(--ink)">EV Chargers</h4><p class="p">Power your car at home.</p><ul><li>1. Approved smart units</li><li>2. Smart off-peak charging</li><li>3. Connect with your app</li></ul><span class="btn">Learn More</span></div>
      <div class="svc"><div class="img" role="img" aria-label="Solar panel array under blue sky"></div><span class="icon"></span><h4 style="color:var(--ink)">Heat Pumps</h4><p class="p">Heat your home efficiently.</p><ul><li>1. Certified local installer</li><li>2. Free performance check</li><li>3. Help with grant forms</li></ul><span class="btn">Learn More</span></div>
    </div>
  </section>

  <section class="steps">
    <div class="wrap center">
      <span class="tag">Working Process</span>
      <h2 class="h2">Easy Steps For <em>Solar And</em><br>Renewable Energy</h2>
      <div class="underline"></div>
      <div class="step-row" style="text-align:left">
        <div class="step"><div class="pill">Step - 01</div><span class="icon"></span><h4>Choose Service</h4><p class="p">Pick the system that suits your home and the way you use energy.</p></div>
        <div class="step"><div class="pill">Step - 02</div><span class="icon"></span><h4>Free Consultant</h4><p class="p">Our advisor visits, checks your roof and explains every option.</p></div>
        <div class="step"><div class="pill">Step - 03</div><span class="icon"></span><h4>Planing &amp; Analysis</h4><p class="p">We model output and savings, then agree a clear fixed quote.</p></div>
        <div class="step"><div class="pill">Step - 04</div><span class="icon"></span><h4>Solar Installation</h4><p class="p">Certified fitters install, test and hand over your new system.</p></div>
      </div>
    </div>
  </section>

  <section class="skills">
    <div class="wrap">
      <div class="skills-art"><div class="img" role="img" aria-label="Technician working on rooftop solar panels among trees"></div></div>
      <div class="skills-copy">
        <span class="tag">Our Skills</span>
        <h2 class="h2">We Offers Solar <em>That's<br>Easy</em> And Efficient.</h2>
        <p class="p">Years of hands-on experience mean every install is neat, safe and tuned for the best possible output from your roof.</p>
        <div class="bar"><div class="row"><span>Solar Panels</span><span>85%</span></div><div class="track"><div class="fill" style="width:85%"></div></div></div>
        <div class="bar"><div class="row"><span>Solar Installation</span><span>65%</span></div><div class="track"><div class="fill" style="width:65%"></div></div></div>
        <div class="bar"><div class="row"><span>Renewable Energy</span><span>75%</span></div><div class="track"><div class="fill" style="width:75%"></div></div></div>
        <span class="btn">Learn More</span>
      </div>
    </div>
  </section>

  <section class="portfolio">
    <div class="wrap center">
      <span class="tag">Our Portfolio</span>
      <h2 class="h2">Let's Check Our Latest<br>Portfolio</h2>
      <div class="folio-row" style="text-align:left">
        <div class="folio"><div class="img" role="img" aria-label="Row of wind turbines at sunset" style="background:linear-gradient(180deg,#d7cbb6,#b7a58a 60%,#6d6554)"></div><div class="cap"><div><small>RENEWABLE</small><b>Hydraulic Energy</b></div><span class="go">↗</span></div></div>
        <div class="folio"><div class="img" role="img" aria-label="Engineer in orange workwear checking panels" style="background:linear-gradient(180deg,#4f8ed9,#e28b3a 55%,#2c4f7f)"></div><div class="cap"><div><small>MAINTENANCE</small><b>Solar Maintenance</b></div><span class="go">↗</span></div></div>
        <div class="folio"><div class="img" role="img" aria-label="Installers on a roof of solar panels" style="background:linear-gradient(180deg,#6ea6e6,#b5cfe9 40%,#3460a8)"></div><div class="cap"><div><small>SOLAR PANEL</small><b>Solar Panels Energy</b></div><span class="go">↗</span></div></div>
        <div class="folio"><div class="img" role="img" aria-label="Solar farm beside a power station" style="background:linear-gradient(180deg,#cfa36c,#8a6a4b 50%,#37415a)"></div><div class="cap"><div><small>WIND POWER</small><b>Wind Generators</b></div><span class="go">↗</span></div></div>
      </div>
    </div>
  </section>

  <section class="pricing">
    <div class="wrap center">
      <span class="tag">Pricing Plan</span>
      <h2 class="h2">Let's Check Our <em>Pricing</em><br>Plan For You</h2>
      <div class="underline"></div>
      <div class="plans" style="text-align:left">
        <div class="plan"><span class="flag">Basic</span><div class="price">$359<small>/Monthly</small></div><span class="btn">Purchase Now</span><ul><li>Crystalline Cell Materials</li><li>Reliability And Performance</li><li>Just In Time Manufacturing</li><li>24/7 Customers Support</li><li>Solar Material Financing</li><li>75% More Energy Output</li></ul></div>
        <div class="plan featured"><span class="flag">Standard</span><div class="price">$559<small>/Monthly</small></div><span class="btn">Purchase Now</span><ul><li>Crystalline Cell Materials</li><li>Reliability And Performance</li><li>Just In Time Manufacturing</li><li>24/7 Customers Support</li><li>Solar Material Financing</li><li>75% More Energy Output</li></ul></div>
        <div class="plan"><span class="flag">Premium</span><div class="price">$959<small>/Monthly</small></div><span class="btn">Purchase Now</span><ul><li>Crystalline Cell Materials</li><li>Reliability And Performance</li><li>Just In Time Manufacturing</li><li>24/7 Customers Support</li><li>Solar Material Financing</li><li>75% More Energy Output</li></ul></div>
      </div>
    </div>
  </section>

  <section class="stats">
    <div class="wrap">
      <div class="stat"><span class="icon"></span><div><b>150<sup>+</sup></b><small>Projects Done</small></div></div>
      <div class="stat"><span class="icon"></span><div><b>25<sup>k</sup></b><small>Happy Clients</small></div></div>
      <div class="stat"><span class="icon"></span><div><b>120<sup>+</sup></b><small>Experts Staff</small></div></div>
      <div class="stat"><span class="icon"></span><div><b>50<sup>+</sup></b><small>Win Awards</small></div></div>
    </div>
  </section>

  <section class="team">
    <div class="wrap center">
      <span class="tag">Our Team</span>
      <h2 class="h2">Meet With Our <em>Experts</em></h2>
      <div class="underline"></div>
      <div class="members">
        <div class="member"><div class="img" role="img" aria-label="Team member portrait in hard hat" style="background:linear-gradient(180deg,#3a6fc0,#e07a3a)"></div><span class="plus"></span><b>Rowan Castell</b><small>Project Manager</small></div>
        <div class="member"><div class="img" role="img" aria-label="Team member portrait in hi-vis vest" style="background:linear-gradient(180deg,#8fb3d8,#d9c23f)"></div><span class="plus"></span><b>Milo Harte</b><small>CEO &amp; Founder</small></div>
        <div class="member"><div class="img" role="img" aria-label="Team member portrait in safety helmet" style="background:linear-gradient(180deg,#c9d3dc,#6c7a8a)"></div><span class="plus"></span><b>Ada Brennan</b><small>Marketing Manager</small></div>
        <div class="member"><div class="img" role="img" aria-label="Team member portrait in blue workwear" style="background:linear-gradient(180deg,#4b7fc4,#1f3d78)"></div><span class="plus"></span><b>Bella Dunmore</b><small>Electric Engineer</small></div>
        <div class="member"><div class="img" role="img" aria-label="Team member portrait in orange workwear" style="background:linear-gradient(180deg,#a9c7e6,#e3733a)"></div><span class="plus"></span><b>Dean Ellery</b><small>Systems Engineer</small></div>
      </div>
    </div>
  </section>

  <section class="quote">
    <div class="quote-img" role="img" aria-label="Installers fitting solar panels under a bright sky"><span class="play"></span></div>
    <div class="quote-form">
      <h3>Request A Quote</h3>
      <p class="p" style="margin-top:4px">Tell us about your home and we will send a free, no-obligation quote within two working days.</p>
      <div class="fields">
        <div class="field">Name</div><div class="field">Email</div>
        <div class="field">Phone</div><div class="field">Choose Service ⌄</div>
        <div class="field wide">Your Message</div>
      </div>
      <span class="btn">Request A Quote</span>
    </div>
  </section>

  <section class="sustain on-dark">
    <div class="wrap">
      <h2 class="h2">We Provide Sustainable &amp; Reliable<br>Energy Systems</h2>
      <p class="p">Join thousands of UK households already saving with clean, dependable power from Brightvale Energy.</p>
      <span class="btn">Contact Now</span>
    </div>
    <div class="logos"><span>Verdra</span><span>Solvo</span><span>Leafline</span><span>Homewise</span><span>Verdra</span><span>Solvo</span></div>
  </section>

  <section class="why">
    <div class="wrap">
      <div class="why-copy">
        <span class="tag">Why Choose Us</span>
        <h2 class="h2">We Deliver <em>Expertise You</em><br><em>Can Trust</em> Our Service</h2>
        <p class="p">We are a trusted local installer focused on quality work, honest advice and long-term support.</p>
        <div class="reason"><span class="icon"></span><div><h4>Affordable Cost</h4><p class="p">Fair prices and finance options that make switching simple.</p></div></div>
        <div class="reason"><span class="icon"></span><div><h4>Our Experience Team</h4><p class="p">Skilled engineers with thousands of homes completed.</p></div></div>
        <div class="reason"><span class="icon"></span><div><h4>Certified Company</h4><p class="p">Fully accredited, insured and backed by warranties.</p></div></div>
      </div>
      <div class="why-art">
        <div class="a" role="img" aria-label="Wind turbines above a green field"></div>
        <div class="b" role="img" aria-label="Workers installing rooftop solar panels"></div>
      </div>
    </div>
  </section>

  <section class="testi on-dark">
    <div class="wrap">
      <div class="testi-intro">
        <span class="tag">Testimonials</span>
        <h2 class="h2">What Our Client<br><em>Say's</em> About Us</h2>
        <p class="p">Real words from homeowners who made the switch to cleaner, cheaper energy with our team.</p>
        <span class="btn">Read More</span>
      </div>
      <div class="review"><div class="stars">★★★★★</div><q>The team were tidy, friendly and quick. Our bills have dropped and the battery keeps us going every evening without any fuss.</q><b>Maya Pemberton</b><small>Customer</small></div>
      <div class="review"><div class="stars">★★★★★</div><q>Clear advice from start to finish. The heat pump and panels work perfectly and the aftercare has been first class so far.</q><b>Declan Pryce</b><small>Customer</small><span class="av" role="img" aria-label="Customer avatar"></span></div>
      <div class="dots"><i></i><i></i></div>
    </div>
  </section>

  <section class="blog">
    <div class="wrap center">
      <span class="tag">Our Blog</span>
      <h2 class="h2">Our Latest News &amp; <em>Blog</em></h2>
      <div class="underline"></div>
      <div class="posts" style="text-align:left">
        <div class="post"><div class="img" role="img" aria-label="Solar panels under the sun" style="background:linear-gradient(160deg,#f4d35e,#3b78c8 45%,#1c3b72)"><span class="date">05 Jun</span></div><div class="meta">By Alma Dorne · 2.5k Comments</div><h4>How Much Can Solar Save A Typical UK Home?</h4><p class="p">A simple look at real savings and payback times.</p><span class="btn">Read More</span></div>
        <div class="post"><div class="img" role="img" aria-label="Engineer in orange vest on solar roof" style="background:linear-gradient(160deg,#7fb2e8,#e0833c 55%,#3a5d96)"><span class="date">05 Jun</span></div><div class="meta">By Alma Dorne · 1.5k Comments</div><h4>Choosing The Right Home Battery Size For You</h4><p class="p">What to consider before you add storage.</p><span class="btn">Read More</span></div>
        <div class="post"><div class="img" role="img" aria-label="Solar farm at dusk near power plant" style="background:linear-gradient(160deg,#e7b36a,#7a5a42 50%,#2c3550)"><span class="date">05 Jun</span></div><div class="meta">By Alma Dorne · 2.5k Comments</div><h4>Heat Pumps Explained: Grants And Running Costs</h4><p class="p">Everything you need to know before switching.</p><span class="btn">Read More</span></div>
      </div>
    </div>
  </section>

  <footer class="footer">
    <div class="wrap">
      <div class="foot-brand">
        <div class="brand">Brightvale <span>Energy</span></div>
        <p class="p">Lighting the path of UK homes sustainably with solar, storage, EV charging and heat pumps.</p>
        <h5>Subscribe Our Newsletter</h5>
        <div class="sub"><span>✉ Your Email</span><span class="btn">Subscribe</span></div>
      </div>
      <div class="foot-col"><h5>Company</h5><ul><li>About Us</li><li>Update News</li><li>Testimonials</li><li>Contact Us</li><li>Terms Of Service</li><li>Privacy policy</li></ul></div>
      <div class="foot-col"><h5>Services</h5><ul><li>Solar Panels</li><li>Wind Generators</li><li>Easy Installation</li><li>Solar Maintenance</li><li>Hydraulic Power</li><li>Fossil Resources</li></ul></div>
      <div class="foot-col"><h5>Get In Touch</h5>
        <div class="contact"><span class="icon"></span><div><b>Our Address</b><br>14 Harrow Lane, Bristol, UK</div></div>
        <div class="contact"><span class="icon"></span><div><b>Call Us</b><br>+44 20 7946 0321</div></div>
        <div class="contact"><span class="icon"></span><div><b>Mail Us</b><br>hello@brightvaleenergy.co.uk</div></div>
      </div>
    </div>
    <div class="foot-bottom"><span>© Copyright 2025 Brightvale Energy All Rights Reserved.</span><span class="social"><i></i><i></i><i></i><i></i></span></div>
  </footer>

</div>
</body>
</html>
```